THE PRACTICE NAME "The Corvane MD" FOR A NEW MEDICAL PRACTICE STARTUP

THIS IS A BUSINESS CARD REQUEST FOR A KIDNEY DOCTOR's(NEPHROLOGIST) PRACTICE, THIS PRACTICE WILL BE IN EL PASO,TEXAS USA.OPEN TO INNOVATIVE IDEAS!

THE CORVANE MD ( NAME OF PRACTICE)

DEVESH R. MALHOTRA, MD FNKF FASN ( NAME OF PHYSICIAN WITH DEGREES)
BOARD CERTIFIED INTERNAL MEDICINE
BOARD CERTIFIED NEPHROLOGY
HYPERTENSION SPECIALIST

OFFICE ADDRESS, PHONE, FAX AND EMAIL PENDING

Saving Kidneys. Saving Lives.(MOTTO) THE LOGO SHOILD REFLECT THIS MESSAGE. WE NEED A LOGO DESIGN WITH 2 KIDNEYS OR CAN BE ONE KIDNEY ALSO.

Target Market(s)

PATIENTS WITH KIDNEY DISEASE, HYPERTENSION, ENGLISH AND SPANISH SPEAKING POPULATION AND PATIENTS ON DIALYSIS

Industry/Entity Type

Health Care

Contact Information for Business Card

HYPERTENSION SPECIALIST

WEBSITE URL PENDING

Font styles to use
Serif
Sans Serif
Script

Colors
fbed38
ffc214
fbf289
fbee3e
5c5c5c
333333
1b1b1b
757575
d3d3d3

Requirements
Must have
• A KIDNEY LOGO
• NAME OF THE PRACTICE
Nice to have
• IF THE CARD CAN BE IN THE SHAPE OF A KIDNEY

```html
<!DOCTYPE html>
<html lang="en">
<head>
<meta charset="utf-8">
<title>The Corvane MD – Business Card</title>
<link href="https://fonts.googleapis.com/css2?family=Tinos:wght@400;700&family=Montserrat:wght@400;500&display=swap" rel="stylesheet">
<style>
  :root {
    --backdrop: #262626;
    --card: #0b0b0c;
    --blue: #3c93dc;
    --blue-deep: #2f7cc4;
    --blue-bright: #29a3ee;
  }
  * { margin: 0; padding: 0; box-sizing: border-box; }
  html, body {
    width: 1200px; height: 900px; overflow: hidden;
    background: var(--backdrop);
  }
  .card {
    position: absolute; left: 75px; top: 150px;
    width: 1050px; height: 600px;
    background: var(--card);
    color: var(--blue);
    overflow: hidden;
  }
  .physician {
    position: absolute; right: 95px; top: 52px;
    text-align: right;
    font-family: "Tinos", "Times New Roman", serif;
  }
  .physician-name {
    font-weight: 700; font-size: 40px; letter-spacing: 1px;
    color: var(--blue-deep); line-height: 1;
  }
  .physician-degrees {
    font-size: 25px; color: var(--blue); margin-top: 4px; line-height: 1;
  }
  .title-rule {
    position: absolute; left: 460px; top: 142px;
    width: 500px; height: 3px; background: var(--blue-deep);
  }
  .credentials {
    position: absolute; right: 90px; top: 166px;
    list-style: none; text-align: right;
    font-family: "Tinos", "Times New Roman", serif;
    font-size: 24px; line-height: 30px; color: var(--blue);
  }
  .credentials li { display: flex; justify-content: flex-end; align-items: center; gap: 14px; }
  .credentials li:nth-child(1) { margin-right: 0; }
  .credentials svg { width: 36px; height: 16px; }
  .practice-mark {
    position: absolute; left: 92px; top: 308px;
    display: flex; align-items: center; gap: 14px;
    font-family: "Montserrat", Arial, sans-serif;
    font-weight: 500; font-size: 30px; color: var(--blue);
  }
  .practice-mark .dot {
    width: 22px; height: 22px; border-radius: 50%; background: var(--blue);
  }
  .divider {
    position: absolute; left: 92px; top: 372px;
    width: 1000px; height: 5px; background: var(--blue);
  }
  .contacts {
    position: absolute; top: 430px;
    list-style: none;
    font-family: "Montserrat", Arial, sans-serif;
    font-size: 27px; color: var(--blue);
  }
  .contacts li { display: flex; align-items: center; gap: 18px; height: 46px; }
  .contacts svg { width: 26px; height: 26px; flex: none; }
  .contacts-left { left: 70px; }
  .contacts-right { left: 600px; }
</style>
</head>
<body>
  <main class="card">
    <header class="physician">
      <div class="physician-name">DEVESH R. MALHOTRA</div>
      <div class="physician-degrees">MD FNKF FASN</div>
    </header>
    <div class="title-rule"></div>

    <ul class="credentials">
      <li><svg viewBox="0 0 36 16"><path d="M0 5h22V0l14 8-14 8v-5H0z" fill="var(--blue-bright)"/></svg>BOARD CERTIFIED INTERNAL MEDICINE</li>
      <li><svg viewBox="0 0 36 16"><path d="M0 5h22V0l14 8-14 8v-5H0z" fill="var(--blue-bright)"/></svg>BOARD CERTIFIED NEPHROLOGY</li>
      <li><svg viewBox="0 0 36 16"><path d="M0 5h22V0l14 8-14 8v-5H0z" fill="var(--blue-bright)"/></svg>HYPERTENSION SPECIALIST</li>
    </ul>

    <div class="practice-mark"><span class="dot"></span>The Corvane MD</div>
    <div class="divider"></div>

    <ul class="contacts contacts-left">
      <li>
        <svg viewBox="0 0 24 24"><path d="M12 2a7 7 0 0 0-7 7c0 5 7 13 7 13s7-8 7-13a7 7 0 0 0-7-7zm0 9.5A2.5 2.5 0 1 1 12 6.5a2.5 2.5 0 0 1 0 5z" fill="var(--blue-bright)"/></svg>
        248, Mesa Court&nbsp; El Paso, Texas, USA
      </li>
      <li>
        <svg viewBox="0 0 24 24"><rect x="2" y="5" width="20" height="14" fill="none" stroke="var(--blue-bright)" stroke-width="2"/><path d="M2 5l10 8 10-8M2 19l7-7M22 19l-7-7" fill="none" stroke="var(--blue-bright)" stroke-width="2"/></svg>
        corvanecare@mailbox.com
      </li>
      <li>
        <svg viewBox="0 0 24 24"><circle cx="12" cy="12" r="10" fill="none" stroke="var(--blue-bright)" stroke-width="2"/><path d="M2 12h20M12 2c3 3 3 17 0 20M12 2c-3 3-3 17 0 20" fill="none" stroke="var(--blue-bright)" stroke-width="1.6"/></svg>
        www.Corvanemd.Com
      </li>
    </ul>

    <ul class="contacts contacts-right">
      <li>
        <svg viewBox="0 0 24 24"><path d="M6.6 10.8a15 15 0 0 0 6.6 6.6l2.2-2.2a1 1 0 0 1 1-.25 11.4 11.4 0 0 0 3.6.6 1 1 0 0 1 1 1V20a1 1 0 0 1-1 1A17 17 0 0 1 3 4a1 1 0 0 1 1-1h3.5a1 1 0 0 1 1 1c0 1.25.2 2.45.6 3.6a1 1 0 0 1-.25 1z" fill="var(--blue-bright)"/></svg>
        0455 318 260
      </li>
      <li>
        <svg viewBox="0 0 24 24"><rect x="6" y="2" width="12" height="20" rx="2" fill="none" stroke="var(--blue-bright)" stroke-width="2"/><rect x="8.5" y="5" width="7" height="5" fill="var(--blue-bright)"/><path d="M9 13h2M13 13h2M9 16h2M13 16h2M9 19h6" stroke="var(--blue-bright)" stroke-width="1.6"/></svg>
        0455 318 260
      </li>
    </ul>
  </main>
</body>
</html>
```